Postcard Design

We are a full service lawn maintenace and landscapig company. Everything from maintenance, fertilizer programs, to design and install.
I would like the card to have a classy look including our logo which is attached. The logo would just have to contain the lettering and the swooshes not the pine tree background if not needed.

Industry/Entity Type

It Company

```html
<!DOCTYPE html>
<html lang="en">
<head>
<meta charset="utf-8">
<title>Silver Birch Landscaping – Postcard</title>
<link href="https://fonts.googleapis.com/css2?family=Tinos:wght@400;700&display=swap" rel="stylesheet">
<style>
  :root{
    --backdrop:#3a3a3a;
    --green-deep:#4f6f4f;
    --green-mid:#7fa57b;
    --green-soft:#b9dcb2;
    --green-pale:#eef5ec;
    --band:#a6d59c;
    --ink:#1f1f1f;
    --white:#ffffff;
  }
  *{margin:0;padding:0;box-sizing:border-box}
  html,body{width:1200px;height:900px;overflow:hidden}
  body{background:var(--backdrop);position:relative;font-family:"Tinos",serif}

  .postcard{position:absolute;overflow:hidden;box-shadow:0 6px 18px rgba(0,0,0,.45)}
  .postcard svg{position:absolute;inset:0;display:block}

  /* Front */
  .postcard--front{left:525px;top:22px;width:630px;height:410px}
  .front__name{position:absolute;left:24px;top:34px;color:var(--white);
    font-family:"Tinos",serif;font-weight:700;font-size:32px;line-height:30px;letter-spacing:2px;text-transform:uppercase;white-space:nowrap}
  .front__contact{position:absolute;left:395px;top:316px;color:var(--white);
    font-family:"Tinos",serif;font-size:19px;line-height:25px;text-transform:uppercase;white-space:nowrap}

  /* Back */
  .postcard--back{left:53px;top:457px;width:635px;height:410px;
    background:linear-gradient(180deg,var(--green-pale) 0%,#dcebd8 52%,#9fc39a 66%,var(--green-mid) 80%,var(--green-deep) 100%)}
  .back__logo-panel{position:absolute;left:20px;top:112px;width:332px;height:146px;
    background:linear-gradient(180deg,#6f8d6c 0%,#8ea48b 45%,#a6b1a2 100%)}
  .back__name{position:absolute;left:24px;top:158px;color:var(--white);
    font-family:"Tinos",serif;font-weight:700;font-size:29px;line-height:30px;letter-spacing:2px;text-transform:uppercase;white-space:nowrap}
  .back__contact{position:absolute;left:130px;top:230px;width:100px;color:var(--white);
    font-family:"Tinos",serif;font-size:9px;line-height:10px;text-align:center;white-space:nowrap}
  .back__divider{position:absolute;left:372px;top:45px;width:2px;height:316px;background:var(--ink)}
  .back__stamp{position:absolute;left:498px;top:50px;width:78px;height:93px;border:1.5px dashed var(--ink)}
  .back__address-line{position:absolute;left:400px;width:176px;height:2px;background:var(--ink)}
</style>
</head>
<body>

<section class="postcard postcard--front" aria-label="Postcard front">
  <svg viewBox="0 0 630 410" width="630" height="410">
    <defs>
      <radialGradient id="front-glow" cx="0.55" cy="0.55" r="0.65">
        <stop offset="0" stop-color="#c6e8be"/>
        <stop offset="0.55" stop-color="#8eb489"/>
        <stop offset="1" stop-color="#56775a"/>
      </radialGradient>
      <linearGradient id="photo-crew-tone" x1="0" y1="0" x2="0" y2="1">
        <stop offset="0" stop-color="#6b7a52"/>
        <stop offset="1" stop-color="#a08a72"/>
      </linearGradient>
      <linearGradient id="photo-trucks-tone" x1="0" y1="0" x2="0" y2="1">
        <stop offset="0" stop-color="#9a958b"/>
        <stop offset="1" stop-color="#6e6258"/>
      </linearGradient>
    </defs>
    <rect class="front__background" width="630" height="410" fill="url(#front-glow)"/>
    <path class="front__band" d="M360 0 C410 140 520 195 630 188 L630 0 Z" fill="var(--band)" opacity=".55"/>
    <path class="front__photo" role="img" aria-label="Photo of a crew member unloading fertilizer bags in a field"
      d="M382 0 C430 120 525 180 630 176 L630 0 Z" fill="url(#photo-crew-tone)"/>
    <path class="front__band" d="M0 164 C185 150 330 265 375 410 L0 410 Z" fill="var(--band)"/>
    <path class="front__photo" role="img" aria-label="Photo of delivery trucks on a road beneath mountains"
      d="M0 174 C170 168 300 280 350 410 L0 410 Z" fill="url(#photo-trucks-tone)"/>
  </svg>
  <h1 class="front__name">Silver Birch<br>Landscaping</h1>
  <p class="front__contact">18210 Maple Crest<br>Ferndale, MI 48220<br>586-555-0137</p>
</section>

<section class="postcard postcard--back" aria-label="Postcard back">
  <div class="back__logo-panel" role="img" aria-label="Faded photo of a pine tree line"></div>
  <h2 class="back__name">Silver Birch<br>Landscaping</h2>
  <p class="back__contact">18210 Maple Crest<br>Ferndale, MI 48220<br>586-555-0137</p>
  <div class="back__divider"></div>
  <div class="back__stamp"></div>
  <div class="back__address-line" style="top:170px"></div>
  <div class="back__address-line" style="top:207px"></div>
  <div class="back__address-line" style="top:246px"></div>
  <div class="back__address-line" style="top:286px"></div>
</section>

</body>
</html>
```